Post Card Design Bright Lantern Youth

We need a postcard design that will be mailed to all residents offering free pickups of donated clothing. Our foundation is called Bright Lantern Youth, we are a nonprofit charitable organization that provides meals and medical services to children in need in Honduras. Collecting unwanted second-hand clothing generates revenue that helps fund the mission and programs run by our foundation. We would like to offer our pickup services to everyone who has any unwanted reusable clothing.

```html
<!DOCTYPE html>
<html lang="en">
<head>
<meta charset="utf-8">
<title>Free Pickups of Donated Clothing – Postcard</title>
<link rel="stylesheet" href="https://fonts.googleapis.com/css2?family=Fredoka:wght@500;600&family=Roboto+Condensed:ital,wght@0,400;1,300;1,400&display=swap">
<style>
  :root{
    --pink:#e6198a;
    --blue:#1190dc;
    --blue-dark:#0a78c2;
    --green:#8cc63f;
    --green-light:#b9dd7a;
    --white:#ffffff;
    --ink:#222222;
    --stage:#e8e8e9;
    --stamp:#a9a9ab;
  }
  *{box-sizing:border-box;margin:0;padding:0}
  html,body{width:1200px;height:1117px;overflow:hidden;background:var(--stage)}
  .postcard{position:absolute;top:383px;width:540px;height:350px;background:var(--white);overflow:hidden;box-shadow:0 2px 6px rgba(0,0,0,.12)}
  .postcard--front{left:50px}
  .postcard--back{left:610px}
  .card-art{position:absolute;inset:0;width:540px;height:350px}
  .headline{position:absolute;left:37px;top:20px;font-family:"Fredoka",sans-serif;font-weight:600;font-size:35px;line-height:33px;color:var(--pink)}
  .intro{position:absolute;left:37px;top:142px;width:220px;font-family:"Roboto Condensed",sans-serif;font-style:italic;font-weight:300;font-size:16px;line-height:17.5px;color:var(--ink)}
  .brand-name{position:absolute;font-family:"Fredoka",sans-serif;font-weight:600;color:var(--green);text-align:center;line-height:1.05}
  .front-brand{left:259px;top:200px;width:110px;font-size:15px}
  .back-brand{left:352px;top:60px;width:96px;font-size:14px}
  .contact-title{font-family:"Fredoka",sans-serif;font-weight:600;color:var(--white);font-size:16px}
  .phone{display:flex;align-items:center;gap:6px;font-family:"Fredoka",sans-serif;font-weight:600;color:var(--white);font-size:25px;line-height:1}
  .phone svg{width:22px;height:22px;flex:none}
  .front-contact{position:absolute;left:37px;top:293px}
  .front-contact .contact-title{margin-left:29px}
  .details{font-family:"Roboto Condensed",sans-serif;font-size:12px;color:var(--white);line-height:15px}
  .detail{display:flex;align-items:flex-start;gap:5px}
  .detail svg{width:9px;height:11px;flex:none;margin-top:2px}
  .front-address{position:absolute;left:246px;top:306px;padding-right:10px;border-right:1px solid var(--white)}
  .front-web{position:absolute;left:375px;top:306px}
  .mission{position:absolute;left:33px;top:27px;width:240px;font-family:"Roboto Condensed",sans-serif;font-style:italic;font-weight:300;font-size:15px;line-height:14.5px;color:var(--ink)}
  .goal{position:absolute;left:20px;top:103px;width:270px;font-family:"Roboto Condensed",sans-serif;font-style:italic;font-weight:400;font-size:10px;line-height:11px;color:var(--white);text-align:center}
  .back-contact{position:absolute;left:33px;top:238px}
  .back-contact .contact-title{margin-left:29px}
  .back-contact .details{margin-top:3px;margin-left:10px}
  .back-contact .detail svg{margin-right:8px}
  .stamp-box{position:absolute;left:463px;top:23px;width:56px;height:56px;background:var(--stamp)}
</style>
</head>
<body>

<section class="postcard postcard--front" aria-label="Postcard front">
  <svg class="card-art" viewBox="0 0 540 350" xmlns="http://www.w3.org/2000/svg">
    <defs>
      <linearGradient id="kidsPhoto" x1="0" y1="0" x2="0" y2="1">
        <stop offset="0" stop-color="#4f6b35"/>
        <stop offset=".45" stop-color="#8a8f88"/>
        <stop offset="1" stop-color="#6fa23a"/>
      </linearGradient>
    </defs>
    <path role="img" aria-label="Photo of a large group of children standing outdoors on grass" d="M272,0 H540 V272 H300 L306,190 C338,112 330,44 272,0 Z" fill="url(#kidsPhoto)"/>
    <path d="M262,0 C326,44 338,112 302,196" fill="none" stroke="var(--green)" stroke-width="9"/>
    <path d="M0,262 C110,222 220,228 320,252 C420,270 490,258 540,240 V262 C480,280 410,282 320,268 C220,252 110,250 0,282 Z" fill="var(--green)"/>
    <path d="M0,282 C120,250 230,262 330,276 C430,288 490,270 540,254 V350 H0 Z" fill="var(--blue)"/>
    <circle cx="314" cy="222" r="67" fill="var(--white)" stroke="var(--blue)" stroke-width="6"/>
  </svg>

  <h1 class="headline">Free Pickups<br>Of Donated<br>Clothing</h1>
  <p class="intro">We are a nonprofit charitable organization that provides meals and medical services to children in need in Honduras.</p>
  <p class="brand-name front-brand">Bright Lantern Youth</p>

  <div class="front-contact">
    <p class="contact-title">Contact Us Today!</p>
    <p class="phone">
      <svg viewBox="0 0 24 24"><circle cx="12" cy="12" r="10.5" fill="none" stroke="#fff" stroke-width="1.8"/><path d="M8.2 6.6l2 .2 1 2.6-1.3 1.1c.7 1.5 1.7 2.5 3.2 3.2l1.1-1.3 2.6 1 .2 2c-.5.8-1.4 1.2-2.3 1-3.8-.8-6.6-3.6-7.4-7.4-.2-.9.2-1.8.9-2.4z" fill="#fff"/></svg>
      (555) 214-3370
    </p>
  </div>
  <div class="details front-address">
    <div class="detail"><svg viewBox="0 0 10 12"><path d="M5 0.5a4 4 0 0 0-4 4c0 3 4 7 4 7s4-4 4-7a4 4 0 0 0-4-4zm0 5.5a1.5 1.5 0 1 1 0-3 1.5 1.5 0 0 1 0 3z" fill="#fff"/></svg><span>18 Maple Works Rd.<br>Riverton, NJ 07000</span></div>
  </div>
  <div class="details front-web">
    <div class="detail"><svg viewBox="0 0 12 12"><circle cx="6" cy="6" r="5" fill="none" stroke="#fff"/><path d="M1 6h10M6 1c-2.5 3-2.5 7 0 10M6 1c2.5 3 2.5 7 0 10" fill="none" stroke="#fff" stroke-width=".8"/></svg><span>https://brightlanternyouth.org</span></div>
    <div class="detail"><svg viewBox="0 0 12 12"><rect x="1" y="2.5" width="10" height="7" fill="none" stroke="#fff"/><path d="M1 2.5l5 4 5-4" fill="none" stroke="#fff"/></svg><span>info@brightlanternyouth.org</span></div>
  </div>
</section>

<section class="postcard postcard--back" aria-label="Postcard back">
  <svg class="card-art" viewBox="0 0 540 350" xmlns="http://www.w3.org/2000/svg">
    <defs>
      <clipPath id="backPanel">
        <path d="M0,0 H290 C322,90 312,200 300,262 C290,310 272,330 258,350 H0 Z"/>
      </clipPath>
      <linearGradient id="teamPhoto" x1="0" y1="0" x2="0" y2="1">
        <stop offset="0" stop-color="#6f8f8a"/>
        <stop offset=".5" stop-color="#c9c3bb"/>
        <stop offset="1" stop-color="#e9e6e2"/>
      </linearGradient>
    </defs>
    <g clip-path="url(#backPanel)">
      <rect x="0" y="92" width="320" height="55" fill="var(--pink)"/>
      <rect role="img" aria-label="Photo of the foundation team in white shirts" x="0" y="151" width="320" height="78" fill="url(#teamPhoto)"/>
      <rect x="0" y="233" width="320" height="117" fill="var(--blue)"/>
    </g>
    <path d="M312,0 C346,90 336,200 324,262 C314,310 296,330 282,350" fill="none" stroke="var(--green)" stroke-width="22"/>
    <path d="M330,0 C362,90 352,200 340,262 C330,310 312,330 298,350" fill="none" stroke="var(--green-light)" stroke-width="6"/>
    <path d="M292,0 C324,90 314,200 302,262 C292,310 274,330 260,350" fill="none" stroke="var(--pink)" stroke-width="6"/>
  </svg>

  <p class="mission">Collecting unwanted second-hand clothing generates revenue that helps fund the mission and programs run by our foundation.</p>
  <p class="goal">In the long term, our goal is to help communities create sustainable kitchens by providing the resources and support they need to get started.</p>

  <div class="back-contact">
    <p class="contact-title">Contact Us Today!</p>
    <p class="phone">
      <svg viewBox="0 0 24 24"><circle cx="12" cy="12" r="10.5" fill="none" stroke="#fff" stroke-width="1.8"/><path d="M8.2 6.6l2 .2 1 2.6-1.3 1.1c.7 1.5 1.7 2.5 3.2 3.2l1.1-1.3 2.6 1 .2 2c-.5.8-1.4 1.2-2.3 1-3.8-.8-6.6-3.6-7.4-7.4-.2-.9.2-1.8.9-2.4z" fill="#fff"/></svg>
      (555) 214-3370
    </p>
    <div class="details">
      <div class="detail"><svg viewBox="0 0 10 12"><path d="M5 0.5a4 4 0 0 0-4 4c0 3 4 7 4 7s4-4 4-7a4 4 0 0 0-4-4zm0 5.5a1.5 1.5 0 1 1 0-3 1.5 1.5 0 0 1 0 3z" fill="#fff"/></svg><span>18 Maple Works Rd. Riverton, NJ 07000</span></div>
      <div class="detail"><svg viewBox="0 0 12 12"><rect x="1" y="2.5" width="10" height="7" fill="none" stroke="#fff"/><path d="M1 2.5l5 4 5-4" fill="none" stroke="#fff"/></svg><span>info@brightlanternyouth.org</span></div>
      <div class="detail"><svg viewBox="0 0 12 12"><circle cx="6" cy="6" r="5" fill="none" stroke="#fff"/><path d="M1 6h10M6 1c-2.5 3-2.5 7 0 10M6 1c2.5 3 2.5 7 0 10" fill="none" stroke="#fff" stroke-width=".8"/></svg><span>https://brightlanternyouth.org</span></div>
    </div>
  </div>

  <p class="brand-name back-brand">Bright Lantern Youth</p>
  <div class="stamp-box" aria-hidden="true"></div>
</section>

</body>
</html>
```